Paper Lighthouse Book Cover

Copper Wren Publishers is looking for a book cover suitable for their new release "The Paper Lighthouse". A modern detective story set in Los Angeles with a science fiction overlay. The book is the first of a series, and subsequent editions will need covers which match the first. The back cover text summarizes the plot.

Must deliver files suitable for Adobe Illustrator, matching the included cover template.

Target Market(s)

People who like science fiction and noir detective stories

Font styles to use
Serif

```html
<!DOCTYPE html>
<html lang="en">
<head>
<meta charset="utf-8">
<title>The Paper Lighthouse – Cover Spread</title>
<link rel="stylesheet" href="https://fonts.googleapis.com/css2?family=Alfa+Slab+One&family=Crimson+Text:wght@400;600&display=swap">
<style>
  :root {
    --jacket-black: #231f20;
    --paper-white: #ffffff;
    --title-orange: #f7941d;
    --outline-black: #111111;
    --sky-grey: #9aa0a6;
    --tower-grey: #6d747b;
    --tower-dark: #1c2128;
    --street-dark: #24272c;
    --glow-amber: #e08a2c;
  }
  * { margin: 0; padding: 0; box-sizing: border-box; }
  html, body { width: 1200px; height: 904px; overflow: hidden; background: var(--jacket-black); }
  .spread { position: relative; width: 1200px; height: 904px; background: var(--jacket-black); color: var(--paper-white); font-family: "Crimson Text", Georgia, serif; }

  /* Back cover */
  .author-portrait {
    position: absolute; left: 48px; top: 54px; width: 210px; height: 282px;
    border: 6px solid var(--paper-white);
    background: linear-gradient(160deg, #d8d8d8 0%, #9a9a9a 45%, #3a3a3a 100%);
  }
  .author-bio {
    position: absolute; left: 273px; top: 52px; width: 252px;
    font-size: 14.4px; line-height: 16.4px;
  }
  .author-bio .indent { padding-left: 38px; }
  .author-bio a { color: var(--paper-white); text-decoration: underline; }
  .blurb {
    position: absolute; left: 34px; top: 440px; width: 500px;
    font-size: 18px; line-height: 22px;
  }
  .blurb p + p { margin-top: 7px; }
  .publisher {
    position: absolute; left: 65px; top: 714px; width: 120px; height: 161px;
    border: 5px solid var(--paper-white);
    display: flex; flex-direction: column; align-items: center; justify-content: flex-end;
    padding-bottom: 10px; gap: 10px;
  }
  .publisher-square { width: 56px; height: 56px; background: var(--paper-white); }
  .publisher-name { font-size: 17px; line-height: 18px; text-align: center; color: var(--paper-white); }

  /* Spine */
  .spine {
    position: absolute; left: 566px; top: 0; width: 74px; height: 904px;
    display: flex; justify-content: center; padding-top: 60px;
  }
  .spine-text {
    writing-mode: vertical-rl;
    font-family: "Alfa Slab One", "Rockwell", serif;
    font-size: 34px; letter-spacing: 0.5px; white-space: nowrap;
  }
  .spine-author { color: var(--paper-white); margin-bottom: 44px; }
  .spine-title { color: var(--title-orange); }

  /* Front cover */
  .front { position: absolute; left: 640px; top: 0; width: 560px; height: 904px; overflow: hidden; }
  .front-scene {
    position: absolute; inset: 0;
    background:
      radial-gradient(ellipse 38% 22% at 28% 80%, rgba(224,138,44,0.85) 0%, rgba(224,138,44,0) 100%),
      radial-gradient(ellipse 25% 30% at 12% 62%, rgba(200,120,40,0.5) 0%, rgba(200,120,40,0) 100%),
      linear-gradient(90deg, var(--tower-dark) 0%, #2a3140 20%, rgba(42,49,64,0) 26%),
      linear-gradient(90deg, rgba(0,0,0,0) 30%, #2b2f36 36%, rgba(0,0,0,0) 48%),
      linear-gradient(90deg, rgba(0,0,0,0) 62%, var(--tower-grey) 72%, #5a6168 100%),
      linear-gradient(180deg, var(--sky-grey) 0%, #7c838a 45%, var(--street-dark) 80%, #1a1c20 100%);
  }
  .front-author {
    position: absolute; left: 0; right: 0; top: 50px; text-align: center;
    font-family: "Alfa Slab One", "Rockwell", serif; font-size: 50px; line-height: 1;
    color: var(--paper-white); letter-spacing: 1px;
    text-shadow: -2px 0 #111, 2px 0 #111, 0 -2px #111, 0 2px #111, 3px 3px 2px rgba(0,0,0,0.6);
  }
  .front-title {
    font-family: "Alfa Slab One", "Rockwell", serif; color: var(--title-orange);
    font-weight: 400; line-height: 1;
  }
  .front-title span {
    position: absolute; left: 0; right: 0; text-align: center; display: block;
    text-shadow: -3px 0 var(--outline-black), 3px 0 var(--outline-black), 0 -3px var(--outline-black), 0 3px var(--outline-black),
                 -2px -2px var(--outline-black), 2px -2px var(--outline-black), -2px 2px var(--outline-black), 2px 2px var(--outline-black),
                 5px 5px 3px rgba(0,0,0,0.55);
  }
  .front-title .line-the { top: 113px; font-size: 84px; }
  .front-title .line-paper { top: 184px; font-size: 80px; }
  .front-title .line-lighthouse { top: 262px; font-size: 70px; }
</style>
</head>
<body>
<main class="spread">
  <section class="back-cover">
    <div class="author-portrait" role="img" aria-label="Black and white portrait of the author holding a black cat, with a small bird on her shoulder"></div>
    <div class="author-bio">
      <p>R.M. Vale is an award-winning painter, performer, writer, and naturalist - She’ll do anything that won’t pay the bills, especially if it involves animals.</p>
      <p class="indent">Leon Hartwell called her stories,</p>
      <p>“…marvelously inventive, wildly funny and deeply thought-provoking. I cannot recommend them highly enough.” She’s been published widely, including Starwell Quarterly. Her stories are on Orbitline’s 2019 and 2020, Year’s Best Stories list. She's been nominated for five Lanternfold awards in 2021. She's shown her art at the Harbor Museum of Art, and Internationally, and would be quite happy if you'd buy some. Check out paintings, writing, musings, and books at <a>www.rmvalestudio.com</a> and <a>bookmarket.example/author/rmvale</a>.</p>
    </div>
    <div class="blurb">
      <p>Meet Eddie Evers: a hard-drinking PI with a talent for finding missing children. While on a case, Eddie is hit by lightning, super-charging the biophotons in his brain and opening his eyes to other dimensions. Electric and electronic devices now tend to misbehave in Eddie's presence as well.</p>
      <p>Assisted by a savant cat named Max, a Sikh taxi driver called Singh, and a secret society of scientists, Eddie treks through the dark alleys and hilltop mansions of Los Angeles trying to discover who’s been killing elementary school teachers and students. Can he solve solve the case and save lives or will his glimpses into other times, places, and dimensions trap him within his own mind?</p>
    </div>
    <div class="publisher">
      <div class="publisher-square"></div>
      <div class="publisher-name">Copper Wren Publishers</div>
    </div>
  </section>

  <section class="spine">
    <div class="spine-text">
      <span class="spine-author">R.M. VALE</span>
      <span class="spine-title">THE PAPER LIGHTHOUSE</span>
    </div>
  </section>

  <section class="front">
    <div class="front-scene" role="img" aria-label="Dusky city street at twilight: dark glass towers on the left, grey skyscrapers on the right, glowing yellow taxis, a man in a dark coat on the crosswalk and a black cat beside him"></div>
    <div class="front-author">R.M. VALE</div>
    <h1 class="front-title">
      <span class="line-the">THE</span>
      <span class="line-paper">PAPER</span>
      <span class="line-lighthouse">LIGHTHOUSE</span>
    </h1>
  </section>
</main>
</body>
</html>
```